Marlow Fields Thank-You Tag

Looking for a file that incorporates current branding/colors and says:

"Thanks for Swimming with Us!"
Marlow Fields Otters

Samples of other pieces we've done recently are attached.

Will be printed on cardstock that is
Width: 3.5 inches
Height: 2.5 inches

```html
<!DOCTYPE html>
<html lang="en">
<head>
<meta charset="utf-8">
<title>Marlow Fields Otters – Thank-You Tag</title>
<link rel="stylesheet" href="https://fonts.googleapis.com/css2?family=Fira+Sans:wght@700&display=swap">
<style>
  :root {
    --page: #e6e7e9;
    --pool-blue: #4a6bbf;
    --splash-blue: #9fd0ee;
    --foam-white: #ffffff;
    --otter-pink: #ee6fb5;
    --ink-white: #ffffff;
  }
  * { margin: 0; padding: 0; box-sizing: border-box; }
  html, body {
    width: 1200px; height: 900px; overflow: hidden;
    background: var(--page);
  }
  .tag {
    position: absolute; left: 100px; top: 93px;
    width: 1000px; height: 714px;
    border-radius: 42px; overflow: hidden;
    background: var(--pool-blue);
    font-family: "Fira Sans", Arial, sans-serif;
  }
  .tag__wave { position: absolute; inset: 0; width: 100%; height: 100%; }
  .tag__headline {
    position: absolute; left: 60px; top: 92px; width: 780px;
    color: var(--ink-white); font-weight: 700;
    font-size: 62px; line-height: 1.05; text-align: center;
    text-transform: uppercase; letter-spacing: 0.5px;
    white-space: nowrap;
  }
  .tag__splash {
    position: absolute; left: 420px; top: 238px;
    width: 60px; height: 30px; border-radius: 50% 50% 8px 8px;
    background: var(--splash-blue);
  }
  .tag__club {
    position: absolute; left: 200px; top: 284px; width: 500px;
    text-align: center; color: var(--otter-pink); font-weight: 700;
    text-transform: uppercase; line-height: 1;
  }
  .tag__club-place { display: block; font-size: 32px; letter-spacing: 3px; }
  .tag__club-team { display: block; font-size: 104px; letter-spacing: 1px; margin-top: 2px; }
  .tag__mascot {
    position: absolute; border-radius: 40%;
    background: linear-gradient(135deg, #ffffff 0%, #c9d6f2 55%, #ee6fb5 100%);
    opacity: 0.9;
  }
  .tag__mascot--left { left: 120px; top: 440px; width: 120px; height: 120px; }
  .tag__mascot--right { left: 770px; top: 230px; width: 140px; height: 110px; }
</style>
</head>
<body>
  <main class="tag">
    <svg class="tag__wave" viewBox="0 0 1000 714" preserveAspectRatio="none" aria-hidden="true">
      <defs>
        <path id="wave-shape" d="M0,610 C150,590 300,602 430,565 C580,520 660,450 790,440 C880,434 940,410 1000,385 L1000,714 L0,714 Z"/>
      </defs>
      <use href="#wave-shape" fill="var(--splash-blue)" transform="translate(0,-6)"/>
      <use href="#wave-shape" fill="var(--foam-white)" transform="translate(0,6)"/>
      <use href="#wave-shape" fill="var(--otter-pink)" transform="translate(0,34)"/>
    </svg>

    <h1 class="tag__headline">Thanks for<br>Swimming with Us!</h1>

    <div class="tag__splash" role="img" aria-label="Small water splash drops"></div>

    <p class="tag__club">
      <span class="tag__club-place">Marlow Fields</span>
      <span class="tag__club-team">Otters</span>
    </p>

    <div class="tag__mascot tag__mascot--left" role="img" aria-label="Leaping swimmer mascot with pink burst"></div>
    <div class="tag__mascot tag__mascot--right" role="img" aria-label="Diving swimmer mascot with pink burst"></div>
  </main>
</body>
</html>
```